5 post cards for B2B Advertising

We are an electrical lighting contractor advertising our Lighting and Electrical services to property management companies, car dealer ships, hotels, schools, malls, and shopping centers.

RED / White / Blue themed American flag.

Post Cards

1. Electrical Services
2. Lighting Services and conversions to LED
3. Sign Repairs and conversions to LED
4. Nighttime Lighting Inspections (report lights and signs out)
5. Lighting is Safety

```html
<!DOCTYPE html>
<html lang="en">
<head>
<meta charset="utf-8">
<title>Voltmere Lighting Co. – Postcard Set</title>
<link href="https://fonts.googleapis.com/css2?family=Exo+2:wght@800&family=Open+Sans:wght@400;700&display=swap" rel="stylesheet">
<style>
:root{
  --blue:#2b3595;
  --red:#ec1c24;
  --white:#ffffff;
  --board:#b3b3b3;
  --guide:#2fb36b;
  --ink:#1a1a1a;
  --stamp:#eeeeee;
}
*{margin:0;padding:0;box-sizing:border-box}
html,body{width:1171px;height:1200px;overflow:hidden;background:var(--board)}
.sheet{position:relative;width:1171px;height:1200px}
.card{position:absolute;width:445px;height:288px;background:var(--white);overflow:hidden;outline:1px solid #d98a8a}
.card .art{position:absolute;left:0;top:0;width:445px;height:288px}
.card .guide{position:absolute;inset:5px;border:1px dashed var(--guide);pointer-events:none}
.c1{left:120px;top:134px}.c2{left:600px;top:134px}
.c3{left:120px;top:458px}.c4{left:600px;top:458px}
.c5{left:120px;top:782px}.c6{left:600px;top:782px}

.brand{position:absolute;width:180px;text-align:center;font-family:"Exo 2",sans-serif;font-weight:800;color:var(--red);line-height:1}
.brand-name{display:block;font-size:27px;letter-spacing:.5px}
.brand-sub{display:block;font-size:10px;letter-spacing:1.5px;margin-top:4px}

.headline{position:absolute;font-family:"Exo 2",sans-serif;font-weight:800;line-height:1.2;text-transform:uppercase}
.headline .b{color:var(--blue)}.headline .r{color:var(--red)}

.body-copy{position:absolute;font-family:"Open Sans",sans-serif;font-size:7px;line-height:9.4px;color:var(--ink)}
.body-copy b{font-weight:700}
.center{text-align:center}

.phone{position:absolute;display:flex;align-items:center;justify-content:center;gap:8px;font-family:"Open Sans",sans-serif;font-weight:700;font-size:22px;color:var(--white);height:36px}
.phone svg{width:20px;height:20px}
.site{position:absolute;font-family:"Open Sans",sans-serif;font-size:8.5px;text-align:center}
.site.red{color:var(--red)}.site.blue{color:var(--blue)}

.stamp{position:absolute;left:380px;top:6px;width:59px;height:58px;background:var(--stamp)}
.address{position:absolute;left:10px;top:258px;width:170px;font-family:"Open Sans",sans-serif;font-weight:700;font-size:5.5px;line-height:7px;color:var(--white);text-align:center}
</style>
</head>
<body>
<div class="sheet">

<!-- Card 1: Electrical Services -->
<section class="card c1">
  <svg class="art" viewBox="0 0 445 288">
    <defs>
      <linearGradient id="c1a" x1="0" y1="0" x2="1" y2="1"><stop offset="0" stop-color="#4a5a72"/><stop offset="1" stop-color="#8e9266"/></linearGradient>
      <linearGradient id="c1b" x1="0" y1="0" x2="1" y2="1"><stop offset="0" stop-color="#7a3b2c"/><stop offset="1" stop-color="#3d3d3d"/></linearGradient>
    </defs>
    <g role="img" aria-label="Electrician in hard hat working inside an electrical panel">
      <polygon points="0,0 172,0 225,145 0,145" fill="url(#c1a)"/>
    </g>
    <polygon points="180,0 189,0 242,145 233,145" fill="var(--blue)"/>
    <polygon points="0,232 265,232 252,268 0,268" fill="var(--blue)"/>
    <polygon points="205,145 214,145 268,288 259,288" fill="var(--red)"/>
    <g role="img" aria-label="Two electricians servicing a wall-mounted panel by a brick building">
      <polygon points="224,145 445,145 445,288 274,288" fill="url(#c1b)"/>
    </g>
  </svg>
  <div class="brand" style="left:241px;top:22px"><span class="brand-name">VOLTMERE</span><span class="brand-sub">LIGHTING CO.</span></div>
  <div class="headline center" style="left:251px;top:92px;width:160px;font-size:15px"><span class="b">Electrical</span><br><span class="r">Services</span></div>
  <p class="body-copy" style="left:22px;top:164px;width:185px"><b>Power Up Your Business</b> with our <b>expert Electrical Services!</b> From energy-efficient lighting to emergency repairs, we are <b>your trusted partner</b>, we ensure your business runs <b>smoothly and safely</b>. Contact us today for <b>reliable service!</b></p>
  <div class="phone" style="left:10px;top:232px;width:210px"><svg viewBox="0 0 20 20"><circle cx="10" cy="10" r="8.6" fill="none" stroke="#fff" stroke-width="1.6"/><path d="M7 5.5l1.6 2.4-1 1.1c.6 1.3 1.5 2.2 2.8 2.8l1.1-1 2.4 1.6-.7 1.6c-3.9.1-7.1-3.1-7-7z" fill="#fff"/></svg>877-555-0148</div>
  <div class="site red" style="left:20px;top:270px;width:190px">www.voltmerelighting.com</div>
  <div class="guide"></div>
</section>

<!-- Card 2: Sports Lighting -->
<section class="card c2">
  <svg class="art" viewBox="0 0 445 288">
    <defs>
      <linearGradient id="c2a" x1="0" y1="0" x2="0" y2="1"><stop offset="0" stop-color="#6f7a80"/><stop offset=".6" stop-color="#9aa2a0"/><stop offset="1" stop-color="#3f8a3a"/></linearGradient>
      <linearGradient id="c2b" x1="0" y1="0" x2="0" y2="1"><stop offset="0" stop-color="#5d88c6"/><stop offset="1" stop-color="#3c5068"/></linearGradient>
    </defs>
    <g role="img" aria-label="Indoor sports facility with LED high-bay fixtures over a turf field">
      <polygon points="224,0 445,0 445,145 274,145" fill="url(#c2a)"/>
    </g>
    <polygon points="249,150 445,150 445,155 251,155" fill="var(--red)"/>
    <g role="img" aria-label="Technician in harness working on stadium light fixtures">
      <polygon points="0,145 169,145 221,288 0,288" fill="url(#c2b)"/>
    </g>
    <polygon points="188,177 194,177 240,288 234,288" fill="var(--blue)"/>
    <polygon points="213,230 445,230 445,266 228,266" fill="var(--red)"/>
  </svg>
  <div class="brand" style="left:34px;top:20px"><span class="brand-name">VOLTMERE</span><span class="brand-sub">LIGHTING CO.</span></div>
  <div class="headline center" style="left:14px;top:84px;width:220px;font-size:12.5px"><span class="r">Sports Lighting</span><br><span class="b">Installation, Repairs, and</span><br><span class="b">Conversions</span> <span class="r">to LED</span></div>
  <p class="body-copy" style="left:229px;top:176px;width:192px">Voltmere Lighting Inc are <b>trusted experts trusted</b> with today’s most critical lighting from Highways lighting to pro stadium lighting, <b>call us today</b>, we will <b>brighten up your world!</b></p>
  <div class="phone" style="left:228px;top:230px;width:210px"><svg viewBox="0 0 20 20"><circle cx="10" cy="10" r="8.6" fill="none" stroke="#fff" stroke-width="1.6"/><path d="M7 5.5l1.6 2.4-1 1.1c.6 1.3 1.5 2.2 2.8 2.8l1.1-1 2.4 1.6-.7 1.6c-3.9.1-7.1-3.1-7-7z" fill="#fff"/></svg>877-555-0148</div>
  <div class="site blue" style="left:235px;top:270px;width:190px">www.voltmerelighting.com</div>
  <div class="guide"></div>
</section>

<!-- Card 3: Sign Repairs -->
<section class="card c3">
  <svg class="art" viewBox="0 0 445 288">
    <defs>
      <linearGradient id="c3a" x1="0" y1="0" x2="0" y2="1"><stop offset="0" stop-color="#7097c9"/><stop offset=".5" stop-color="#b59272"/><stop offset="1" stop-color="#7c2b24"/></linearGradient>
      <linearGradient id="c3b" x1="0" y1="0" x2="0" y2="1"><stop offset="0" stop-color="#2f5a9a"/><stop offset=".6" stop-color="#5a7a5a"/><stop offset="1" stop-color="#3d6a30"/></linearGradient>
    </defs>
    <polygon points="258,0 266,0 217,145 208,145" fill="var(--blue)"/>
    <g role="img" aria-label="Technician in a bucket lift repairing storefront sign lettering">
      <polygon points="276,0 445,0 445,145 226,145" fill="url(#c3a)"/>
    </g>
    <g role="img" aria-label="Bucket trucks servicing a roadside monument sign">
      <polygon points="0,145 221,145 175,288 0,288" fill="url(#c3b)"/>
    </g>
    <polygon points="235,145 243,145 196,288 188,288" fill="var(--red)"/>
    <polygon points="213,227 445,227 445,263 201,263" fill="var(--red)"/>
  </svg>
  <div class="headline" style="left:22px;top:20px;width:220px;font-size:15px"><span class="b">Sign Repairs</span> <span class="r">and</span><br><span class="r">Conversions to LED</span></div>
  <p class="body-copy" style="left:22px;top:67px;width:180px"><b>Light Up the Night</b> with Voltmere Lighting Inc! Whether you need reliable <b>LED security lights</b> or <b>eye-catching signage</b>, our skilled team has got you covered. From commercial properties to pro stadiums, we deliver exceptional <b>outdoor lighting solutions</b> that shine bright.</p>
  <div class="brand" style="left:237px;top:160px"><span class="brand-name">VOLTMERE</span><span class="brand-sub">LIGHTING CO.</span></div>
  <div class="phone" style="left:222px;top:227px;width:210px"><svg viewBox="0 0 20 20"><circle cx="10" cy="10" r="8.6" fill="none" stroke="#fff" stroke-width="1.6"/><path d="M7 5.5l1.6 2.4-1 1.1c.6 1.3 1.5 2.2 2.8 2.8l1.1-1 2.4 1.6-.7 1.6c-3.9.1-7.1-3.1-7-7z" fill="#fff"/></svg>877-555-0148</div>
  <div class="site red" style="left:232px;top:270px;width:190px">www.voltmerelighting.com</div>
  <div class="guide"></div>
</section>

<!-- Card 4: Nighttime Inspections -->
<section class="card c4">
  <svg class="art" viewBox="0 0 445 288">
    <defs>
      <linearGradient id="c4a" x1="0" y1="0" x2="0" y2="1"><stop offset="0" stop-color="#2c3c80"/><stop offset=".6" stop-color="#5a6072"/><stop offset="1" stop-color="#2a2a34"/></linearGradient>
      <linearGradient id="c4b" x1="0" y1="0" x2="1" y2="0"><stop offset="0" stop-color="#2a2620"/><stop offset=".6" stop-color="#4a4438"/><stop offset="1" stop-color="#c8c8c8"/></linearGradient>
    </defs>
    <g role="img" aria-label="Illuminated retail storefront at dusk">
      <polygon points="0,0 172,0 221,145 0,145" fill="url(#c4a)"/>
    </g>
    <polygon points="181,0 189,0 238,145 230,145" fill="var(--red)"/>
    <polygon points="206,145 214,145 265,288 257,288" fill="var(--blue)"/>
    <g role="img" aria-label="Inspector checking parking lot lights at night beside a service van">
      <polygon points="228,145 445,145 445,288 276,288" fill="url(#c4b)"/>
    </g>
    <polygon points="0,227 236,227 249,263 0,263" fill="var(--red)"/>
  </svg>
  <div class="headline center" style="left:234px;top:15px;width:200px;font-size:13px"><span class="r">Nighttime Lighting</span><br><span class="b">Inspections</span></div>
  <p class="body-copy center" style="left:238px;top:55px;width:192px"><b>Brighten your nights</b> with our Night Time Lighting and Sign Inspection Service. Voltmere Lighting Inc ensures your <b>property’s outdoor lighting and signage shines</b> with a thorough, expert evaluation. <b>Free evaluation</b> of your outdoor lighting and signage. <b>Boost visibility, security, and aesthetics</b>. Schedule your complimentary inspection today and light up the night with confidence!</p>
  <div class="brand" style="left:30px;top:160px"><span class="brand-name">VOLTMERE</span><span class="brand-sub">LIGHTING CO.</span></div>
  <div class="phone" style="left:15px;top:227px;width:210px"><svg viewBox="0 0 20 20"><circle cx="10" cy="10" r="8.6" fill="none" stroke="#fff" stroke-width="1.6"/><path d="M7 5.5l1.6 2.4-1 1.1c.6 1.3 1.5 2.2 2.8 2.8l1.1-1 2.4 1.6-.7 1.6c-3.9.1-7.1-3.1-7-7z" fill="#fff"/></svg>877-555-0148</div>
  <div class="site red" style="left:25px;top:270px;width:190px">www.voltmerelighting.com</div>
  <div class="guide"></div>
</section>

<!-- Card 5: Lighting is Safety -->
<section class="card c5">
  <svg class="art" viewBox="0 0 445 288">
    <defs>
      <linearGradient id="c5a" x1="0" y1="0" x2="1" y2="1"><stop offset="0" stop-color="#2f70c0"/><stop offset=".6" stop-color="#8aa6c0"/><stop offset="1" stop-color="#4a5a40"/></linearGradient>
      <linearGradient id="c5b" x1="0" y1="0" x2="1" y2="1"><stop offset="0" stop-color="#12284a"/><stop offset="1" stop-color="#3a5a7a"/></linearGradient>
    </defs>
    <polygon points="258,0 266,0 217,145 208,145" fill="var(--blue)"/>
    <g role="img" aria-label="Technician servicing a cluster of round pole-top light fixtures">
      <polygon points="276,0 445,0 445,145 226,145" fill="url(#c5a)"/>
    </g>
    <g role="img" aria-label="Lineman relamping a four-head parking lot light at night">
      <polygon points="0,145 221,145 175,288 0,288" fill="url(#c5b)"/>
    </g>
    <polygon points="235,145 243,145 196,288 188,288" fill="var(--red)"/>
    <polygon points="213,227 445,227 445,263 201,263" fill="var(--blue)"/>
  </svg>
  <div class="headline" style="left:22px;top:30px;width:220px;font-size:15px"><span class="r">Lighting</span> <span class="b">is Safety</span></div>
  <p class="body-copy" style="left:22px;top:69px;width:182px"><b>Brighten Every Moment</b> with Voltmere Lighting Inc! Specializing in <b>outdoor lighting</b>. Experience the difference of working with a <b>premier electrical contractor</b> who delivers excellence every time.</p>
  <div class="brand" style="left:245px;top:160px"><span class="brand-name">VOLTMERE</span><span class="brand-sub">LIGHTING CO.</span></div>
  <div class="phone" style="left:228px;top:227px;width:210px"><svg viewBox="0 0 20 20"><circle cx="10" cy="10" r="8.6" fill="none" stroke="#fff" stroke-width="1.6"/><path d="M7 5.5l1.6 2.4-1 1.1c.6 1.3 1.5 2.2 2.8 2.8l1.1-1 2.4 1.6-.7 1.6c-3.9.1-7.1-3.1-7-7z" fill="#fff"/></svg>877-555-0148</div>
  <div class="site red" style="left:240px;top:270px;width:190px">www.voltmerelighting.com</div>
  <div class="guide"></div>
</section>

<!-- Card 6: Mailing side -->
<section class="card c6">
  <svg class="art" viewBox="0 0 445 288">
    <defs>
      <linearGradient id="c6a" x1="0" y1="0" x2="1" y2="1"><stop offset="0" stop-color="#f2f3f6"/><stop offset="1" stop-color="#9aa0b0"/></linearGradient>
    </defs>
    <polygon points="213,0 225,0 175,288 0,288 0,110 194,110" fill="var(--blue)"/>
    <polygon points="0,71 196,71 186,109 0,109" fill="var(--red)"/>
    <g role="img" aria-label="White company service van with ladder rack">
      <rect x="4" y="114" width="196" height="136" rx="4" fill="url(#c6a)"/>
    </g>
    <polygon points="0,251 185,251 178,288 0,288" fill="var(--red)"/>
  </svg>
  <div class="brand" style="left:2px;top:17px"><span class="brand-name" style="font-size:22px">VOLTMERE</span><span class="brand-sub">LIGHTING CO.</span></div>
  <div class="phone" style="left:0;top:72px;width:180px"><svg viewBox="0 0 20 20"><circle cx="10" cy="10" r="8.6" fill="none" stroke="#fff" stroke-width="1.6"/><path d="M7 5.5l1.6 2.4-1 1.1c.6 1.3 1.5 2.2 2.8 2.8l1.1-1 2.4 1.6-.7 1.6c-3.9.1-7.1-3.1-7-7z" fill="#fff"/></svg>877-555-0148</div>
  <p class="address">Voltmere Lighting Inc, 410 Harbor Lane<br>Kestrel Point, NC 27000</p>
  <div class="stamp"></div>
  <div class="guide"></div>
</section>

</div>
</body>
</html>
```